Holistic Psychologist needs contemporary business card

I am a psychologist working with adult clients face to face and online. The card needs to work for clients and also referring doctors and medical professionals. It needs to look warm, safe and trustable for clients, but clean and professional enough for doctors. Sometimes I also work in a corporate context.

I am holistic in my approach (mind-body-spirit) so anything conveying connection or integration or wholeness would be good. But again, clean and contemporary please. It can have a little bit of personality.
New logo uploaded.

Probably warm tones and plenty white space to write on one side.

My web pages:
http://lmtherapy.com.au
https://www.facebook.com/MarcellaWhitfordTherapy?ref=hl
Updates

Hi Designers .. I have decided I do need a new logo before finalising a design for the business cards.  I hope to have this available in 4 days from now.

Kindly,

Marcella

New logo now posted, same brief.  Balance of masculine and feminine elements, plenty of white space on one side please.

Keen to see some card designs, thank-you.

Target Market(s)

Audience 1 - Males and females aged 25 years + seeking counselling or coaching. Audience 2 - doctors and health professionals who refer clients.

Industry/Entity Type

Medical

Contact Information for Business Card

Logo

Marcella Whitford
Registered Psychologist

M: 0491 508 243
www.lmtherapy.com.au
marcella@lmtherapy.com.au
Little blue Facebook icon, with "marcella whitford therapy" printed near it.

Font styles to use
Sans Serif

Requirements
Nice to have
• You might want to play with the words "essential you"
Should not have
• Nothing cutesy or too literal

```html
<!DOCTYPE html>
<html lang="en">
<head>
<meta charset="utf-8">
<title>Marcella Whitford Therapy – Business Card</title>
<link rel="stylesheet" href="https://fonts.googleapis.com/css2?family=Ubuntu:ital,wght@0,400;0,500;1,400&display=swap">
<style>
  :root {
    --navy-deep: #1a2948;
    --navy-mid: #1d5478;
    --navy-band: #19304f;
    --navy-band-low: #2a4877;
    --slate: #7f97b1;
    --slate-light: #8aa2bb;
    --brand-red: #d8282a;
    --name-ice: #c6dcea;
    --white: #ffffff;
    --paper: #ffffff;
  }
  * { margin: 0; padding: 0; box-sizing: border-box; }
  html, body {
    width: 947px; height: 1200px; overflow: hidden;
    background: var(--paper);
    font-family: "Ubuntu", sans-serif;
  }
  .sheet { position: relative; width: 947px; height: 1200px; }

  /* Front side */
  .card-front {
    position: absolute; left: 0; top: 0; width: 947px; height: 584px;
    background: radial-gradient(ellipse 60% 70% at 50% 40%, var(--navy-mid) 0%, #1b3d63 55%, var(--navy-deep) 100%);
    overflow: hidden;
  }
  .card-front .horizon {
    position: absolute; left: 0; right: 0; top: 295px; bottom: 0;
    background: rgba(120,150,190,0.10);
  }
  .brand {
    position: absolute; display: flex; align-items: center;
  }
  .brand-dot {
    border-radius: 50%; background: var(--brand-red); flex: none;
  }
  .brand-text { color: var(--brand-red); font-weight: 400; line-height: 1; }
  .brand-name { display: block; white-space: nowrap; }
  .brand-line { display: block; text-transform: uppercase; white-space: nowrap; }

  .card-front .brand { left: 92px; top: 232px; }
  .card-front .brand-dot { width: 120px; height: 120px; margin-right: 60px; }
  .card-front .brand-name { font-size: 60px; letter-spacing: 0.5px; }
  .card-front .brand-line { font-size: 32px; letter-spacing: 33px; margin-top: 18px; }

  /* Back side */
  .card-back {
    position: absolute; left: 0; top: 616px; width: 947px; height: 584px;
    background: linear-gradient(180deg, var(--slate-light), var(--slate));
  }
  .card-back .brand { left: 487px; top: 66px; }
  .card-back .brand-dot { width: 64px; height: 64px; margin-right: 28px; }
  .card-back .brand-name { font-size: 35px; }
  .card-back .brand-line { font-size: 18px; letter-spacing: 17.5px; margin-top: 10px; }

  .holder { position: absolute; left: 42px; top: 206px; width: 368px; text-align: right; }
  .holder-name { color: var(--name-ice); font-size: 43px; font-weight: 400; text-align: left; white-space: nowrap; }
  .holder-title { color: var(--white); font-size: 19px; font-style: italic; margin-top: 6px; }

  .links {
    position: absolute; left: 92px; top: 428px;
    display: flex; gap: 54px;
    color: #dde9f2; font-size: 30px; white-space: nowrap;
  }
  .phone-band {
    position: absolute; left: 0; right: 0; top: 475px; height: 56px;
    background: var(--navy-band);
    color: var(--name-ice); font-size: 30px; letter-spacing: 1px;
    display: flex; align-items: center; justify-content: center;
  }
  .social-band {
    position: absolute; left: 0; right: 0; top: 531px; height: 53px;
    background: linear-gradient(90deg, #223c66, var(--navy-band-low), #223c66);
    color: var(--name-ice); font-size: 30px;
    display: flex; align-items: center; justify-content: center; gap: 12px;
  }
  .social-square { width: 30px; height: 30px; background: #3b5fa0; border: 2px solid #c6dcea; flex: none; }
</style>
</head>
<body>
<main class="sheet">
  <section class="card-front">
    <div class="horizon"></div>
    <div class="brand">
      <span class="brand-dot"></span>
      <span class="brand-text">
        <span class="brand-name">Marcella Whitford</span>
        <span class="brand-line">Therapy</span>
      </span>
    </div>
  </section>

  <section class="card-back">
    <div class="brand">
      <span class="brand-dot"></span>
      <span class="brand-text">
        <span class="brand-name">Marcella Whitford</span>
        <span class="brand-line">Therapy</span>
      </span>
    </div>

    <div class="holder">
      <p class="holder-name">Marcella Whitford</p>
      <p class="holder-title">Registered Psychologist</p>
    </div>

    <div class="links">
      <span class="web">www.lmtherapy.com.au</span>
      <span class="email">marcella@lmtherapy.com.au</span>
    </div>

    <div class="phone-band">M: 0491 508 243</div>
    <div class="social-band">
      <span class="social-square"></span>
      <span>“marcella whitford therapy”</span>
    </div>
  </section>
</main>
</body>
</html>
```